Banner Ad Design

Design 2 ad banners with animation: 468x60 and 160x160

The 2 ad banners should complement the look, feel and messaging of our new VANTA6 microphone campaign. Any of the product imagery from the homepage can be used as well. For Reference:

1) website: www.brindlewave-acoustics.com

2) print advertising: http://www.brindlewave-acoustics.com/Advertising/UNlike_the_Others_4.5.html

3) email: http://www.brindlewave-acoustics.com/ecampaign/UNlike/v6_sfdb.html

4) Product photo (if needed):
http://www.brindlewave-acoustics.com/images/Hi_Rz/MV-3KT_BL_headset_microphone.jpg

The small banner sizes will present an interesting challege so we can modify the copy as necessary but for the time being, we have:

NEW! VANTA6 Microphones
Tiny Enough. TOUGH Enough.
Delivers a knockout against the others.
GET a KNOCKOUT.

Target Market(s)

Audio production engineers (front of house guys) who manage the audio during live shows. Here is the online magazine for this target market; the 468x60 banner will rotate at the top of this website: http://www.stagerigdaily.com/

Requirements
Must have
• - Brindlewave Acoustics logo: http://www.brindlewave-acoustics.com/images/BWA_logo-R.jpg
• - Call to Action: GET A KNOCKOUT. ref: http://www.brindlewave-acoustics.com/ecampaign/UNlike/v6_sfdb.html

```html
<!DOCTYPE html>
<html lang="en">
<head>
<meta charset="utf-8">
<title>VANTA6 Banner Ads</title>
<link rel="stylesheet" href="https://fonts.googleapis.com/css2?family=Ubuntu:wght@500;700&display=swap">
<style>
  :root {
    --stage: #2b2b2b;
    --ink-dark: #1c1b1b;
    --panel-dark: #252323;
    --accent: #f39a1e;
    --white: #ffffff;
    --photo-light: #d4d4d2;
    --photo-mid: #a7a6a3;
    --photo-dark: #5e5d5a;
    --photo-shadow: #3a3937;
    --button-top: #5a5754;
    --button-bottom: #33302e;
    --button-edge: #8c8985;
  }
  * { box-sizing: border-box; margin: 0; padding: 0; }
  html, body { width: 1200px; height: 558px; overflow: hidden; }
  body {
    background: var(--stage);
    font-family: "Ubuntu", sans-serif;
    position: relative;
  }

  .headline .new { color: var(--accent); }
  .headline .product { color: var(--white); }

  .cta {
    position: absolute;
    display: flex; align-items: center; justify-content: center;
    border: 1.5px solid var(--button-edge);
    border-radius: 4px;
    background: linear-gradient(180deg, var(--button-top), var(--button-bottom));
    color: var(--accent);
    font-weight: 500;
    font-size: 20px;
    box-shadow: 0 1px 3px rgba(0,0,0,0.5);
  }

  /* Square banner 160x160 at 1.5x */
  .banner-square {
    position: absolute;
    left: 478px; top: 27px;
    width: 240px; height: 240px;
    border: 2px solid var(--accent);
    background: var(--ink-dark);
    overflow: hidden;
  }
  .banner-square .headline {
    position: absolute; left: 0; top: 0; width: 100%; height: 70px;
    background: var(--ink-dark);
    text-align: center;
    padding-top: 7px;
  }
  .banner-square .title { font-size: 28px; font-weight: 700; line-height: 31px; }
  .banner-square .subtitle { font-size: 18px; font-weight: 700; color: var(--white); line-height: 24px; }
  .banner-square .photo {
    position: absolute; left: 0; top: 70px; width: 100%; height: 166px;
    background:
      linear-gradient(180deg, rgba(0,0,0,0) 55%, rgba(30,29,28,0.55) 100%),
      linear-gradient(90deg, var(--photo-light) 0%, var(--photo-mid) 40%, var(--photo-dark) 75%, var(--photo-shadow) 100%);
  }
  .banner-square .cta { left: 13px; top: 187px; width: 210px; height: 42px; }

  /* Leaderboard banner 468x60 at 1.5x */
  .banner-wide {
    position: absolute;
    left: 247px; top: 297px;
    width: 702px; height: 91px;
    border-left: 2px solid var(--accent);
    border-bottom: 2px solid var(--accent);
    background: var(--panel-dark);
    overflow: hidden;
  }
  .banner-wide .photo {
    position: absolute; left: 0; top: 0; width: 460px; height: 100%;
    background:
      linear-gradient(180deg, rgba(255,255,255,0.08) 0%, rgba(0,0,0,0.12) 100%),
      linear-gradient(90deg,
        #cdcdcb 0%, #b3b2af 30%, #9d9c99 55%,
        #b8b7b4 66%, #9a9996 78%, var(--photo-dark) 92%, var(--photo-shadow) 100%);
  }
  .banner-wide .headline { position: absolute; left: 30px; top: 12px; }
  .banner-wide .title { font-size: 28px; font-weight: 700; line-height: 31px; }
  .banner-wide .product,
  .banner-wide .subtitle { text-shadow: 0 1px 2px rgba(0,0,0,0.35); }
  .banner-wide .subtitle { font-size: 18px; font-weight: 700; color: var(--white); line-height: 26px; }
  .banner-wide .divider { position: absolute; left: 420px; top: 0; width: 282px; height: 89px; }
  .banner-wide .cta { left: 470px; top: 20px; width: 214px; height: 52px; }
</style>
</head>
<body>

  <section class="banner-square" aria-label="VANTA6 square banner">
    <div class="photo" role="img" aria-label="Photo of a man in glasses wearing a miniature headset microphone, shown in profile"></div>
    <div class="headline">
      <div class="title"><span class="new">NEW!</span> <span class="product">VANTA6</span></div>
      <div class="subtitle">Miniature Microphones</div>
    </div>
    <div class="cta">Get a KNOCKOUT</div>
  </section>

  <section class="banner-wide" aria-label="VANTA6 leaderboard banner">
    <div class="photo" role="img" aria-label="Photo of a man in glasses wearing a miniature headset microphone, shown in profile"></div>
    <svg class="divider" viewBox="0 0 282 89" aria-hidden="true">
      <polygon points="36,0 282,0 282,89 6,89" fill="var(--panel-dark)"/>
      <polygon points="30,0 37,0 7,89 0,89" fill="var(--accent)"/>
    </svg>
    <div class="headline">
      <div class="title"><span class="new">NEW!</span> <span class="product">VANTA6</span></div>
      <div class="subtitle">Miniature Microphones</div>
    </div>
    <div class="cta">Get a KNOCKOUT</div>
  </section>

</body>
</html>
```